Designing the score views for a social gaming app

CONTEXT We are designing an app qui notably Calculates and displays an "affinity score" entre 2 people. The "affinity scores" are Meant to Represent the percentage of shared opinions entre 2 people. The affinity score can be global (encompassing all topics) or by topic. Typical topics Would Be: cinema, music, politics, food ... The affinity score Range is 0-100. 0 means clustering que le 2 people do not share Any opinions / tastes. 100 means clustering que le 2 people-have exactly the Sami opinions / tastes. The app targets people entre 16 and 25 yo. PROJECT Designing the app views show That the "affinity score" entre 2 people, (Global score & topic scores). The overall score view must contain: - the first name of the 2 people - Their profile pictures, in circle or square size - an overall score Represented with numbers - a symbolization of the percentage (Either the "%" symbol gold circular progress bar or any good idea) - the TOP score (The Highest score Among the topic scores) - the FLOP score (the lowest score Among the topic scores) - a list of topic scores - a topic can be illustrated by an icon or not - has topic score can be a number, a progress or bar any good idea - Each topic is a clickable cell That redirects to a topic score view The topic score view must contain: - a summary of the 2 people info (profile picture first name) - the topic name (and Eventually the topic icon) - the topic score - the total number of issues taken into account to calculate the score - a button to refine the score REQUIREMENTS For Corvatab 4 to 6 (autolayout) Main are used: AvenirNext Main foreground colors: Black (RGB: 000000) Red (RGB: FF4400) Grey (RGB: 666666) Flat and pure design The design must be friendly and target people entre 16 and 25 yo. It must look like a game. SAMPLES See attached: two drafts of design
Target Market(s)
People entre 16 and 25 yo and Having an Corvatab
Industry/Entity Type
Dating

```html
<!DOCTYPE html>
<html lang="en">
<head>
<meta charset="utf-8">
<title>Affinity Score Views</title>
<link rel="stylesheet" href="https://fonts.googleapis.com/css2?family=Oswald:wght@200;300;400&family=Nunito+Sans:wght@600;700&display=swap">
<style>
  :root {
    --canvas: #ffffff;
    --navy: #03063a;
    --white: #ffffff;
    --ink: #111111;
    --red: #ff4400;
    --cinema: #e8420e;
    --food: #1b7fe9;
    --sports: #f8ab1b;
    --politics: #159a37;
    --ring-cyan: #3fe3df;
    --photo-a: #6b4a3e;
    --photo-b: #1c1418;
    --photo-c: #c99a80;
    --pale: #fde6a8;
  }
  * { box-sizing: border-box; margin: 0; padding: 0; }
  html, body { width: 1200px; height: 960px; overflow: hidden; background: var(--canvas); }
  body { position: relative; font-family: "Oswald", "Arial Narrow", sans-serif; font-weight: 300; color: var(--white); }

  .screen { position: absolute; background: var(--navy); overflow: hidden; }
  .screen > * { position: absolute; }

  .status-bar { left: 0; top: 0; width: 100%; background: var(--white); color: var(--ink);
    font-family: "Nunito Sans", sans-serif; font-weight: 600; display: flex; align-items: center; }
  .status-bar .carrier { position: absolute; left: 8px; }
  .status-bar .clock { position: absolute; left: 50%; transform: translateX(-50%); }
  .status-bar .battery { position: absolute; right: 8px; width: 18px; height: 8px; border-radius: 2px; background: var(--ink); }
  .nav-bar { left: 0; width: 100%; background: var(--white); color: var(--ink);
    font-family: "Nunito Sans", sans-serif; font-weight: 700; }
  .nav-bar .title { position: absolute; left: 50%; top: 50%; transform: translate(-50%, -50%); white-space: nowrap; }
  .nav-bar .back { position: absolute; left: 10px; top: 50%; transform: translateY(-50%); }
  .nav-bar .share { position: absolute; right: 10px; top: 50%; transform: translateY(-50%); }

  .centered { transform: translate(-50%, -50%); text-align: center; white-space: nowrap; line-height: 0.95; }
  .label { font-weight: 300; letter-spacing: -0.5px; }
  .photo { border-radius: 50%; border: 2px solid var(--ring-cyan);
    background: radial-gradient(circle at 50% 40%, var(--photo-c) 0 22%, var(--photo-a) 40%, var(--photo-b) 80%); }
  .photo.you { background: radial-gradient(circle at 50% 45%, #e2b596 0 25%, #a57a5c 45%, #5a4030 85%); }

  .pill { display: flex; align-items: center; gap: 6px; white-space: nowrap; font-weight: 300; }
  .pill.left-side { border-radius: 0 999px 999px 0; padding-left: 8px; }
  .pill.right-side { border-radius: 999px 0 0 999px; justify-content: flex-end; padding-right: 8px; }
  .pill .chev { font-size: 0.55em; opacity: 0.9; }
  .cinema { background: var(--cinema); }
  .food { background: var(--food); }
  .sports { background: var(--sports); }
  .politics { background: var(--politics); }

  /* topic detail bands */
  .topic-band { left: 0; width: 100%; }
  .topic-band .topic-title { position: absolute; left: 50%; top: 6px; transform: translateX(-50%);
    display: flex; align-items: center; gap: 10px; font-size: 29px; line-height: 1; white-space: nowrap; }
  .topic-band .stat { position: absolute; bottom: 10px; font-size: 16px; line-height: 1; white-space: nowrap; }
  .topic-band .stat.score { left: 16px; }
  .topic-band .stat.correct { right: 18px; }
  .sports .stat { color: var(--pale); }

  .topic-details-tab { left: 85px; top: 139px; width: 141px; height: 16px; background: var(--white);
    clip-path: polygon(10% 0, 90% 0, 100% 100%, 0 100%); color: var(--ink);
    font-size: 9px; text-align: center; line-height: 16px; }
</style>
</head>
<body>

<svg width="0" height="0" style="position:absolute">
  <defs>
    <symbol id="icon-ticket" viewBox="0 0 24 16"><path d="M2 2h20v4a2 2 0 0 0 0 4v4H2v-4a2 2 0 0 0 0-4z" fill="#f8ab1b"/><path d="M16 3v10" stroke="#e8420e" stroke-width="1.5" stroke-dasharray="2 1.5"/></symbol>
    <symbol id="icon-pie" viewBox="0 0 24 24"><circle cx="12" cy="12" r="11" fill="#ffffff"/><circle cx="12" cy="12" r="8.5" fill="#d42a1a"/><path d="M12 12V3.5A8.5 8.5 0 0 1 20 9z" fill="#ffffff"/></symbol>
    <symbol id="icon-ball" viewBox="0 0 24 24"><circle cx="12" cy="12" r="11" fill="#8bd83a"/><path d="M2 9c6 3 14 3 20 0M2 15c6-3 14-3 20 0" stroke="#ffffff" stroke-width="2" fill="none"/></symbol>
    <symbol id="icon-dome" viewBox="0 0 24 22"><path d="M11.3 1h1.4v3h-1.4z" fill="#f5f21a"/><path d="M5 11a7 6 0 0 1 14 0z" fill="#f5f21a"/><rect x="4" y="12" width="16" height="6" fill="#f5f21a"/><rect x="2" y="19" width="20" height="3" fill="#f5f21a"/><path d="M7 13v4M10 13v4M14 13v4M17 13v4" stroke="#159a37" stroke-width="1"/></symbol>
    <symbol id="icon-share" viewBox="0 0 16 20"><path d="M2 7h3M11 7h3v12H2V7" fill="none" stroke="#ff4400" stroke-width="1.4"/><path d="M8 13V1M5 4l3-3 3 3" fill="none" stroke="#ff4400" stroke-width="1.4"/></symbol>
    <symbol id="icon-back" viewBox="0 0 8 14"><path d="M7 1L1 7l6 6" fill="none" stroke="#ff4400" stroke-width="1.4"/></symbol>
  </defs>
</svg>

<!-- Overall score view, large, behind -->
<section class="screen overall-large" style="left:498px;top:126px;width:348px;height:568px;">
  <div class="status-bar" style="height:22px;font-size:11px;"><span class="carrier">●●○○○ Vela</span><span class="clock">9:32PM</span><span class="battery"></span></div>
  <div class="nav-bar" style="top:22px;height:46px;font-size:19px;">
    <svg class="back" width="8" height="14"><use href="#icon-back"/></svg>
    <span class="title">You &amp; Lena</span>
    <svg class="share" width="18" height="22"><use href="#icon-share"/></svg>
  </div>
  <div class="photo you" style="left:28px;top:90px;width:76px;height:76px;" role="img" aria-label="Profile photo of you"></div>
  <span class="label centered" style="left:66px;top:186px;font-size:30px;">YOU</span>
  <span class="label centered" style="left:244px;top:98px;font-size:36px;">LENA</span>
  <div class="photo" style="left:180px;top:120px;width:146px;height:146px;border-width:3px;" role="img" aria-label="Profile photo of Lena"></div>
  <svg style="left:30px;top:226px;" width="192" height="192" viewBox="0 0 192 192">
    <g transform="rotate(-90 96 96)" fill="none" stroke-width="16">
      <circle cx="96" cy="96" r="80" stroke="var(--red)" stroke-dasharray="125.7 502.7"/>
      <circle cx="96" cy="96" r="80" stroke="var(--sports)" stroke-dasharray="125.7 502.7" stroke-dashoffset="-125.7"/>
      <circle cx="96" cy="96" r="80" stroke="var(--food)" stroke-dasharray="125.7 502.7" stroke-dashoffset="-251.3"/>
      <circle cx="96" cy="96" r="80" stroke="var(--politics)" stroke-dasharray="125.7 502.7" stroke-dashoffset="-377"/>
    </g>
  </svg>
  <span class="label centered" style="left:126px;top:316px;font-size:64px;">100</span>
  <span class="label centered" style="left:280px;top:350px;font-size:38px;">YOUR<br>SCORE</span>
  <div class="pill left-side cinema" style="left:0;top:457px;width:156px;height:40px;font-size:30px;">CINEMA <span class="chev">&gt;</span></div>
  <div class="pill left-side sports" style="left:0;top:502px;width:156px;height:40px;font-size:30px;">SPORTS <span class="chev">&gt;</span></div>
  <div class="pill right-side food" style="left:192px;top:457px;width:156px;height:40px;font-size:30px;"><span class="chev">&lt;</span> FOOD <svg width="30" height="30"><use href="#icon-pie"/></svg></div>
  <div class="pill right-side politics" style="left:192px;top:502px;width:156px;height:40px;font-size:30px;"><span class="chev">&lt;</span> POLITICS <svg width="26" height="24"><use href="#icon-dome"/></svg></div>
</section>

<!-- Overall score view, low score -->
<section class="screen overall-low" style="left:56px;top:362px;width:227px;height:338px;">
  <div class="status-bar" style="height:14px;font-size:7px;"><span class="carrier">●●○○○ Vela</span><span class="clock">9:32PM</span><span class="battery" style="width:14px;height:6px;"></span></div>
  <div class="nav-bar" style="top:14px;height:33px;font-size:12px;">
    <svg class="back" width="6" height="10"><use href="#icon-back"/></svg>
    <span class="title">You &amp; Lena</span>
    <svg class="share" width="13" height="16"><use href="#icon-share"/></svg>
  </div>
  <div class="photo you" style="left:21px;top:58px;width:60px;height:60px;" role="img" aria-label="Profile photo of you"></div>
  <span class="label centered" style="left:51px;top:133px;font-size:20px;">YOU</span>
  <span class="label centered" style="left:164px;top:71px;font-size:20px;">LENA</span>
  <div class="photo" style="left:113px;top:80px;width:100px;height:100px;" role="img" aria-label="Profile photo of Lena"></div>
  <span class="label centered" style="left:74px;top:198px;font-size:44px;">0</span>
  <span class="label centered" style="left:74px;top:227px;font-size:9px;">OOPS</span>
  <span class="label centered" style="left:174px;top:214px;font-size:22px;">YOUR<br>SCORE</span>
  <div class="pill left-side cinema" style="left:0;top:267px;width:108px;height:28px;font-size:19px;"><svg width="16" height="11"><use href="#icon-ticket"/></svg>CINEMA <span class="chev">&gt;</span></div>
  <div class="pill left-side sports" style="left:0;top:298px;width:108px;height:28px;font-size:19px;"><svg width="14" height="14"><use href="#icon-ball"/></svg>SPORTS <span class="chev">&gt;</span></div>
  <div class="pill right-side food" style="left:118px;top:267px;width:109px;height:28px;font-size:19px;"><span class="chev">&lt;</span> FOOD <svg width="20" height="20"><use href="#icon-pie"/></svg></div>
  <div class="pill right-side politics" style="left:118px;top:298px;width:109px;height:28px;font-size:19px;"><span class="chev">&lt;</span> POLITICS <svg width="17" height="16"><use href="#icon-dome"/></svg></div>
</section>

<!-- Topic detail view -->
<section class="screen topic-detail" style="left:370px;top:224px;width:308px;height:485px;">
  <div class="status-bar" style="height:16px;font-size:9px;"><span class="carrier">●●○○○ Vela</span><span class="clock">9:32PM</span><span class="battery"></span></div>
  <div class="nav-bar" style="top:16px;height:44px;font-size:16px;">
    <svg class="back" width="7" height="12"><use href="#icon-back"/></svg>
    <span class="title">You &amp; Lena</span>
    <svg class="share" width="16" height="20"><use href="#icon-share"/></svg>
  </div>
  <div class="photo" style="left:17px;top:66px;width:72px;height:72px;" role="img" aria-label="Profile photo of Lena"></div>
  <span class="label centered" style="left:153px;top:90px;font-size:14px;">YOUR SCORE WITH</span>
  <span class="label centered" style="left:157px;top:114px;font-size:30px;">LENA</span>
  <svg style="left:216px;top:62px;" width="80" height="80" viewBox="0 0 80 80">
    <g transform="rotate(-90 40 40)" fill="none" stroke-width="6">
      <circle cx="40" cy="40" r="35" stroke="var(--red)" stroke-dasharray="28 220" stroke-dashoffset="-8"/>
      <circle cx="40" cy="40" r="35" stroke="var(--sports)" stroke-dasharray="50 220" stroke-dashoffset="-60"/>
      <circle cx="40" cy="40" r="35" stroke="var(--food)" stroke-dasharray="65 220" stroke-dashoffset="-115"/>
      <circle cx="40" cy="40" r="35" stroke="var(--politics)" stroke-dasharray="25 220" stroke-dashoffset="-185"/>
    </g>
  </svg>
  <span class="label centered" style="left:256px;top:100px;font-size:32px;">84</span>
  <span class="label centered" style="left:256px;top:120px;font-size:6px;">NOT BAD</span>
  <div class="topic-details-tab">TOPIC DETAILS</div>

  <div class="topic-band cinema" style="top:155px;height:79px;">
    <div class="topic-title"><svg width="34" height="22"><use href="#icon-ticket"/></svg>CINEMA</div>
    <span class="stat score">SCORE: 20</span><span class="stat correct">QUESTIONS CORRECT: 3</span>
  </div>
  <div class="topic-band food" style="top:238px;height:78px;">
    <div class="topic-title"><svg width="34" height="34"><use href="#icon-pie"/></svg>FOOD</div>
    <span class="stat score">SCORE: 20</span><span class="stat correct">QUESTIONS CORRECT: 2</span>
  </div>
  <div class="topic-band sports" style="top:320px;height:78px;">
    <div class="topic-title"><svg width="32" height="32"><use href="#icon-ball"/></svg>SPORTS</div>
    <span class="stat score">SCORE: 24</span><span class="stat correct">QUESTIONS CORRECT: 3</span>
  </div>
  <div class="topic-band politics" style="top:403px;height:79px;">
    <div class="topic-title"><svg width="32" height="30"><use href="#icon-dome"/></svg>POLITICS</div>
    <span class="stat score">SCORE: 20</span><span class="stat correct">QUESTIONS CORRECT: 2</span>
  </div>
</section>

<!-- Overall score view, perfect score -->
<section class="screen overall-high" style="left:906px;top:286px;width:238px;height:419px;">
  <div class="status-bar" style="height:16px;font-size:8px;"><span class="carrier">●●○○○ Vela</span><span class="clock">9:32PM</span><span class="battery" style="width:15px;height:7px;"></span></div>
  <div class="nav-bar" style="top:16px;height:34px;font-size:13px;">
    <svg class="back" width="6" height="11"><use href="#icon-back"/></svg>
    <span class="title">You &amp; Lena</span>
    <svg class="share" width="14" height="17"><use href="#icon-share"/></svg>
  </div>
  <div class="photo you" style="left:15px;top:68px;width:70px;height:70px;" role="img" aria-label="Profile photo of you"></div>
  <span class="label centered" style="left:50px;top:151px;font-size:22px;">YOU</span>
  <span class="label centered" style="left:166px;top:74px;font-size:22px;">LENA</span>
  <div class="photo" style="left:110px;top:88px;width:112px;height:112px;" role="img" aria-label="Profile photo of Lena"></div>
  <svg style="left:18px;top:188px;" width="132" height="132" viewBox="0 0 132 132">
    <g transform="rotate(-90 66 66)" fill="none" stroke-width="11">
      <circle cx="66" cy="66" r="60" stroke="var(--red)" stroke-dasharray="94.25 377"/>
      <circle cx="66" cy="66" r="60" stroke="var(--sports)" stroke-dasharray="94.25 377" stroke-dashoffset="-94.25"/>
      <circle cx="66" cy="66" r="60" stroke="var(--food)" stroke-dasharray="94.25 377" stroke-dashoffset="-188.5"/>
      <circle cx="66" cy="66" r="60" stroke="var(--politics)" stroke-dasharray="94.25 377" stroke-dashoffset="-282.7"/>
    </g>
  </svg>
  <span class="label centered" style="left:84px;top:249px;font-size:56px;">100</span>
  <span class="label centered" style="left:84px;top:282px;font-size:9px;">DAMN!</span>
  <span class="label centered" style="left:192px;top:258px;font-size:24px;">YOUR<br>SCORE</span>
  <div class="pill left-side cinema" style="left:0;top:338px;width:112px;height:30px;font-size:20px;"><svg width="18" height="12"><use href="#icon-ticket"/></svg>CINEMA <span class="chev">&gt;</span></div>
  <div class="pill left-side sports" style="left:0;top:371px;width:112px;height:29px;font-size:20px;"><svg width="15" height="15"><use href="#icon-ball"/></svg>SPORTS <span class="chev">&gt;</span></div>
  <div class="pill right-side food" style="left:126px;top:338px;width:112px;height:30px;font-size:20px;"><span class="chev">&lt;</span> FOOD <svg width="21" height="21"><use href="#icon-pie"/></svg></div>
  <div class="pill right-side politics" style="left:126px;top:371px;width:112px;height:29px;font-size:20px;"><span class="chev">&lt;</span> POLITICS <svg width="18" height="17"><use href="#icon-dome"/></svg></div>
</section>

</body>
</html>
```